Content processing platform needs a new front page design

We need a new front page design for Plumtext.com. Plumtext.com is a free content processing platform that helps online businesses and freelancers scale their production of content and translation. See pdf for a mockup on what we wish to communicate and layout of the front page. The final design should communicate scalability/growth and we hope to see a design where the user clicks one of the links for iGaming, e-shop, agency in the middle. 60% of our traffic is from mobile devices..

Number of Pages Required

1 page

Font styles to use
Other font styles liked:
• open sans

```html
<!DOCTYPE html>
<html lang="en">
<head>
<meta charset="utf-8">
<title>Plumtext – Scale your content production</title>
<link href="https://fonts.googleapis.com/css2?family=Montserrat:wght@500;600;700;800&family=Open+Sans:wght@400;600;700&display=swap" rel="stylesheet">
<style>
:root{
  --pink:#f2416b;
  --blue:#1f8ccc;
  --blue-dark:#1a74ad;
  --navy:#16324a;
  --ink:#2e3440;
  --muted:#7a8290;
  --light:#f5f7f9;
  --white:#ffffff;
}
*{margin:0;padding:0;box-sizing:border-box}
html,body{width:711px;height:1200px;overflow:hidden}
body{font-family:"Open Sans",sans-serif;color:var(--ink);background:var(--white);position:relative}
.h{font-family:"Montserrat",sans-serif;font-weight:800;letter-spacing:.5px}

/* header */
.site-header{height:38px;display:flex;align-items:center;padding:0 40px;justify-content:space-between;background:var(--white)}
.brand{font-family:"Montserrat",sans-serif;font-weight:800;font-size:17px;color:var(--pink)}
.nav{display:flex;gap:22px;font-size:8px;font-weight:700;color:var(--ink);font-family:"Montserrat",sans-serif}
.btn{display:inline-block;font-family:"Montserrat",sans-serif;font-weight:700;font-size:7.5px;padding:7px 14px;border-radius:2px;color:var(--white);letter-spacing:.4px}
.btn-pink{background:var(--pink)}
.btn-ghost{border:1px solid var(--white);background:transparent}

/* hero */
.hero{position:relative;height:302px;overflow:hidden}
.hero-photo{position:absolute;inset:0;background:linear-gradient(120deg,#8a8f96 0%,#c7b9a8 35%,#e9e1d6 55%,#a99683 80%,#6d6a68 100%)}
.hero-shade{position:absolute;inset:0;background:linear-gradient(90deg,rgba(20,24,30,.55),rgba(20,24,30,.15) 70%)}
.hero-copy{position:absolute;left:40px;top:118px;width:340px;color:var(--white)}
.hero-copy h1{font-size:17px;line-height:1.25;margin-bottom:10px}
.hero-copy p{font-size:7.5px;line-height:1.55;margin-bottom:14px;opacity:.95}
.hero-copy .btn{margin-right:8px}

/* crowd band */
.crowd{height:52px;background:var(--blue);color:var(--white);text-align:center;padding-top:12px}
.crowd h3{font-size:9px;margin-bottom:5px}
.crowd p{font-size:7px}

/* scale */
.scale{height:134px;text-align:center;padding-top:22px}
.section-title{font-size:14px;color:var(--ink);margin-bottom:20px}
.scale-list{display:flex;justify-content:center;gap:58px}
.scale-item{font-size:8px;color:var(--ink);display:flex;flex-direction:column;align-items:center;gap:8px}
.scale-item svg{width:26px;height:26px}

/* clients */
.clients{height:56px;background:var(--blue-dark);display:flex;align-items:center;justify-content:space-around;padding:0 30px}
.client{font-family:"Montserrat",sans-serif;font-weight:700;font-size:13px;color:var(--white)}

/* why */
.why{height:172px;text-align:center;padding-top:26px;background:var(--light)}
.why-list{display:flex;justify-content:center;gap:70px}
.why-item{width:130px;display:flex;flex-direction:column;align-items:center}
.why-item svg{width:24px;height:24px;margin-bottom:8px}
.why-item h4{font-size:9px;font-weight:700;margin-bottom:6px}
.why-item p{font-size:7px;line-height:1.5;color:var(--muted)}

/* signup */
.signup{position:relative;height:128px;text-align:center;color:var(--white);overflow:hidden}
.signup-photo{position:absolute;inset:0;background:linear-gradient(100deg,#2a7fb8,#4aa6dc 50%,#2476ad)}
.signup-inner{position:relative;padding-top:28px}
.signup h2{font-size:16px;margin-bottom:6px}
.signup p{font-size:8px;margin-bottom:12px}

/* testimonials */
.users{height:196px;text-align:center;padding-top:24px}
.users .section-title{margin-bottom:16px}
.quote{width:440px;margin:0 auto 16px;font-size:7.5px;line-height:1.6;color:var(--muted);font-style:italic;position:relative}
.quote::before{content:"\201C";position:absolute;left:-22px;top:-8px;font-size:30px;color:var(--blue);font-style:normal}
.people{display:flex;justify-content:center;gap:60px}
.person{display:flex;align-items:center;gap:7px;text-align:left}
.avatar{width:26px;height:26px;border-radius:50%;background:#c9ced4}
.person b{display:block;font-size:7.5px}
.person span{font-size:6.5px;color:var(--muted)}

/* footer */
.site-footer{height:122px;background:var(--navy);color:#b8c4d0;padding:18px 40px 0;position:relative}
.foot-cols{display:flex;gap:80px}
.foot-col h5{font-family:"Montserrat",sans-serif;font-size:7.5px;color:var(--white);margin-bottom:6px}
.foot-col li{list-style:none;font-size:6.5px;line-height:1.6}
.copyright{position:absolute;left:40px;bottom:10px;font-size:6.5px}
.social{position:absolute;right:40px;bottom:8px;display:flex;gap:6px}
.social span{width:10px;height:10px;border-radius:50%;background:#b8c4d0}
</style>
</head>
<body>

<header class="site-header">
  <div class="brand">plumtext</div>
  <nav class="nav"><span>PRODUCTS ▾</span><span>APPS ▾</span><span>BLOG</span><span>HELP CENTER</span></nav>
  <span class="btn btn-pink">SIGN IN</span>
</header>

<section class="hero">
  <div class="hero-photo" role="img" aria-label="Photo of a smiling team working together at laptops"></div>
  <div class="hero-shade"></div>
  <div class="hero-copy">
    <h1 class="h">SCALE YOUR PRODUCTION OF CONTENT AND TRANSLATION WITH OUR FREE PLATFORM</h1>
    <p>Plumtext is a free platform for businesses and freelancers.<br>Businesses: scale your content production and translation with our crowd.<br>Freelancers: find paid writing and translation work every day.</p>
    <span class="btn btn-pink">BECOME A FREELANCER</span><span class="btn btn-ghost">SCALE PRODUCTION</span>
  </div>
</section>

<section class="crowd">
  <h3 class="h">LATEST CONTENT FROM THE CROWD</h3>
  <p>A new article was just delivered in Swedish · 2 minutes ago</p>
</section>

<section class="scale">
  <h2 class="h section-title">WHAT DO YOU WANT TO SCALE ?</h2>
  <div class="scale-list">
    <div class="scale-item"><svg viewBox="0 0 26 26" fill="none" stroke="#1f8ccc" stroke-width="1.6"><rect x="2" y="8" width="22" height="11" rx="5"/><path d="M8 11v5M5.5 13.5h5"/><circle cx="17" cy="12" r="1"/><circle cx="19.5" cy="15" r="1"/></svg>iGaming</div>
    <div class="scale-item"><svg viewBox="0 0 26 26" fill="none" stroke="#1f8ccc" stroke-width="1.6"><path d="M2 4h4l3 12h12l2-8H8"/><circle cx="10" cy="20" r="1.6"/><circle cx="19" cy="20" r="1.6"/></svg>eShop</div>
    <div class="scale-item"><svg viewBox="0 0 26 26" fill="none" stroke="#1f8ccc" stroke-width="1.6"><circle cx="13" cy="13" r="10"/><path d="M3 13h20M13 3c-4 5-4 15 0 20M13 3c4 5 4 15 0 20"/></svg>New Markets</div>
    <div class="scale-item"><svg viewBox="0 0 26 26" fill="none" stroke="#1f8ccc" stroke-width="1.6"><rect x="3" y="8" width="20" height="14" rx="1.5"/><path d="M9 8V5h8v3M3 14h20"/></svg>Agency</div>
    <div class="scale-item"><svg viewBox="0 0 26 26" fill="none" stroke="#1f8ccc" stroke-width="1.6"><circle cx="13" cy="8" r="4.5"/><path d="M4 23c1-5 5-8 9-8s8 3 9 8"/></svg>Professional Freelancing</div>
  </div>
</section>

<section class="clients">
  <span class="client">NORTHWAY</span>
  <span class="client">lumohome</span>
  <span class="client">FJORDLY</span>
  <span class="client">brightvale</span>
  <span class="client">Kettleroom</span>
  <span class="client">Dunmore</span>
</section>

<section class="why">
  <h2 class="h section-title">WHY ONLINE BUSINESSES USE PLUMTEXT</h2>
  <div class="why-list">
    <div class="why-item"><svg viewBox="0 0 24 24" fill="none" stroke="#f2416b" stroke-width="1.6"><circle cx="12" cy="12" r="10"/><path d="M15 8.5c-1-1-5-1.5-5.5 1s5 2 5 4.5-4.5 2.5-6 1M12 6v12"/></svg><h4>30% cheaper</h4><p>Online businesses using Plumtext save on average 30% on their content and translation costs.</p></div>
    <div class="why-item"><svg viewBox="0 0 24 24" fill="none" stroke="#f2416b" stroke-width="1.6"><circle cx="12" cy="12" r="10"/><path d="M12 6v6l4 2"/></svg><h4>2x faster</h4><p>With a crowd of freelancers, texts and translations are delivered twice as fast.</p></div>
    <div class="why-item"><svg viewBox="0 0 24 24" fill="none" stroke="#f2416b" stroke-width="1.6"><circle cx="12" cy="12" r="3.5"/><path d="M12 2v4M12 18v4M2 12h4M18 12h4M5 5l3 3M16 16l3 3M19 5l-3 3M8 16l-3 3"/></svg><h4>100% automated</h4><p>Plumtext tools and automated workflows plug into your shop and publishing.</p></div>
  </div>
</section>

<section class="signup">
  <div class="signup-photo" role="img" aria-label="Blue-tinted photo of people working at a desk"></div>
  <div class="signup-inner">
    <h2 class="h">SIGN UP NOW</h2>
    <p>Try for yourself, without charge</p>
    <span class="btn btn-ghost">GET STARTED IT'S FREE</span>
  </div>
</section>

<section class="users">
  <h2 class="h section-title">WHAT OUR USERS ARE SAYING</h2>
  <p class="quote">After years of trying agencies, we finally found a way to grow our content without growing our team. We now order articles and translations for every market in minutes, and the quality from the crowd is consistently strong. Plumtext has become a key part of how we work.</p>
  <div class="people">
    <div class="person"><div class="avatar" role="img" aria-label="User portrait"></div><div><b>Anna</b><span>Content manager</span></div></div>
    <div class="person"><div class="avatar" role="img" aria-label="User portrait"></div><div><b>Mikael</b><span>Freelance writer</span></div></div>
    <div class="person"><div class="avatar" role="img" aria-label="User portrait"></div><div><b>Sofie</b><span>Agency owner</span></div></div>
  </div>
</section>

<footer class="site-footer">
  <div class="foot-cols">
    <div class="foot-col"><h5>PLUMTEXT</h5><ul><li>About Us</li><li>Team</li><li>Contact</li><li>Terms of Service</li><li>Privacy Policy</li></ul></div>
    <div class="foot-col"><h5>RESOURCES</h5><ul><li>Plumtext Affiliate</li><li>Content Tools</li><li>Developer Resources</li><li>Plumtext Plugins</li><li>Blog</li></ul></div>
    <div class="foot-col"><h5>CONTACT</h5><ul><li>Plumtext ApS</li><li>Harbour Street 12</li><li>1000 Northby</li><li>Tel: +00 00 00 00 00</li><li>hello@plumtext.com</li></ul></div>
    <div class="foot-col"><h5>LANGUAGES</h5><ul><li>English</li><li>Danish</li></ul></div>
  </div>
  <div class="copyright">© 2018 Plumtext. All Rights Reserved.</div>
  <div class="social"><span></span><span></span><span></span><span></span></div>
</footer>

</body>
</html>
```